Art work Revision to the Current 50 Hz Catalog to 60 Hz Catalog

To change some of the contents from the current 50 Hz catalog to the new 60 Hz catalog. New curves and new data

Colors

Designer to choose colors to be used in the design.

```html
<!DOCTYPE html>
<html lang="en">
<head>
<meta charset="utf-8">
<title>4" KV Submersible Pumps – 60 Hz Catalog Pages</title>
<link href="https://fonts.googleapis.com/css2?family=Roboto+Condensed:wght@300;400;700&family=Roboto:wght@400;700&display=swap" rel="stylesheet">
<style>
  :root{
    --ink:#1d1d1d;
    --muted:#555;
    --rule:#333;
    --band:#efefef;
    --head:#d4d4d4;
    --grid:#c4c4c4;
    --pill:#3b3b3b;
    --brand:#bdbdbd;
    --paper:#ffffff;
  }
  *{box-sizing:border-box;margin:0;padding:0}
  html,body{width:938px;height:1200px;overflow:hidden;background:var(--paper)}
  body{position:relative;font-family:"Roboto",Arial,sans-serif;color:var(--ink)}
  .page{position:absolute;width:396px;height:553px;border:1px solid var(--rule);background:var(--paper)}
  .p9{left:45px;top:27px}.p10{left:469px;top:27px}.p11{left:45px;top:611px}.p12{left:469px;top:611px}
  .brand{position:absolute;left:283px;top:30px;width:92px;font-family:"Roboto Condensed",sans-serif;font-weight:400;font-size:15px;line-height:18px;color:var(--brand);letter-spacing:.5px;text-align:right}
  .series-title{position:absolute;left:38px;top:24px;font-family:"Roboto Condensed",sans-serif;font-weight:400;font-size:15px;line-height:18px;color:#111}
  .band{position:absolute;left:23px;width:350px;height:31px;background:var(--band);display:flex;align-items:center;justify-content:center;font-family:"Roboto Condensed",sans-serif;font-size:12.5px;color:#111;white-space:nowrap}
  .p9 .band{top:86px}.p10 .band{top:66px}.p11 .band,.p12 .band{top:67px}
  .section-drawing{position:absolute;left:43px;top:142px;width:310px;height:128px;background:linear-gradient(180deg,#e8e8e8,#d2d2d2 50%,#e8e8e8)}
  .folio{position:absolute;top:531px;font-size:8px;color:#222}
  .p9 .folio,.p11 .folio{right:18px}.p10 .folio,.p12 .folio{left:14px}
  .charts{position:absolute;left:0;top:0}
  .charts text{font-family:"Roboto",Arial,sans-serif;font-size:5.3px;fill:#444}
  .charts .axis-end{text-anchor:end}
  .charts .axis-mid{text-anchor:middle}
  .curve{fill:none;stroke:#111;stroke-width:.8}
  .frame{fill:none;stroke:#666;stroke-width:.5}
  .pill rect{fill:var(--pill)}
  .charts .pill text{fill:#fff;font-size:4.4px;text-anchor:middle}

  .parts{position:absolute;left:72px;top:292px;width:251px;border-collapse:collapse;table-layout:fixed;font-size:5.7px;color:#333;border:1px solid #ccc}
  .parts col.ref{width:32px}.parts col.desc{width:100px}.parts col.mat{width:119px}
  .parts th{background:var(--head);font-weight:400;height:16.5px;font-size:6.8px;color:#111;border-right:1px solid #fff}
  .parts td{height:10.4px;line-height:10.4px;padding:0 0 0 9px;border-right:1px solid #ccc;white-space:nowrap;overflow:hidden}
  .parts td:first-child{text-align:center;padding-left:0}
  .parts tbody tr:first-child td{height:14px;padding-top:4px}

  .spec{position:absolute;border-collapse:collapse;font-size:4.8px;color:#222;text-align:center;table-layout:auto}
  .spec th,.spec td{border:.5px solid #bbb;padding:0 1px;white-space:nowrap}
  .spec th{font-weight:700;background:#fff;height:9px;line-height:1.15}
  .spec td{height:9.4px;line-height:9px}
  .spec .head-cell{background:#e4e4e4;font-weight:700;writing-mode:vertical-rl;transform:rotate(180deg)}
  .spec td.type{text-align:left;padding-left:2px}
  .p10 .spec{left:70px;top:453px;width:256px}
  .p11 .spec{left:60px;top:435px;width:275px}
  .p12 .spec{left:61px;top:444px;width:274px}
</style>
</head>
<body>

<section class="page p9">
  <h1 class="series-title">4" KV FLOATING STACK<br>IMPELLERS PUMPS SERIES</h1>
  <div class="brand">ORLENTIS</div>
  <div class="band">Cross Sectional Drawing and Parts List for KV 12 and 16</div>
  <div class="section-drawing" role="img" aria-label="Cross sectional technical drawing of the 4 inch KV pump with numbered part callouts"></div>
  <table class="parts">
    <colgroup><col class="ref"><col class="desc"><col class="mat"></colgroup>
    <thead><tr><th>Ref. N.</th><th>Description</th><th>Material</th></tr></thead>
    <tbody>
      <tr><td>1</td><td>Sleeve</td><td>Stainless Steel</td></tr>
      <tr><td>2</td><td>Lower Support/ Motor Adapter</td><td>Casted Stainless Steel</td></tr>
      <tr><td>3</td><td>Discharge Head</td><td>Casted Stainless Steel</td></tr>
      <tr><td>4</td><td>Shaft with Coupling</td><td>Stainless Steel</td></tr>
      <tr><td>5</td><td>Intermediate Support</td><td>Glass Filled Engineered Composites</td></tr>
      <tr><td>6</td><td>Bowl</td><td>Stainless Steel</td></tr>
      <tr><td>7</td><td>Impeller</td><td>Glass Filled PPE Resin</td></tr>
      <tr><td>8</td><td>Diffuser</td><td>Glass Filled Polycarbonate</td></tr>
      <tr><td>9</td><td>Top Diffuser</td><td>Glass Filled Polycarbonate</td></tr>
      <tr><td>10</td><td>Top Bearing</td><td>N.B.R.</td></tr>
      <tr><td>11</td><td>Top Bushing</td><td>Stainless Steel</td></tr>
      <tr><td>12</td><td>Shaft Bushing/Spacer</td><td>Stainless Steel / PPE Resin</td></tr>
      <tr><td>13</td><td>Adapter Ring</td><td>Stainless Steel</td></tr>
      <tr><td>14</td><td>Valve Cap/Non Return Valve</td><td>Stainless Steel</td></tr>
      <tr><td>16</td><td>Valve Support with Gasket</td><td>Stainless Steel and N.B.R.</td></tr>
      <tr><td>17</td><td>Valve Lock Ring</td><td>Stainless Steel</td></tr>
      <tr><td>18</td><td>Filter</td><td>Stainless Steel</td></tr>
      <tr><td>19</td><td>Cable Guard</td><td>Stainless Steel</td></tr>
      <tr><td>21</td><td>Upper Split Ring/Shaft Clip Ring</td><td>Stainless Steel</td></tr>
      <tr><td>23</td><td>Thrust Washer</td><td>Stainless Steel</td></tr>
    </tbody>
  </table>
  <div class="folio">9</div>
</section>

<section class="page p10">
  <div class="brand">ORLENTIS</div>
  <div class="band">4” KV 1 | 4” Submersible Pumps | 50 Hz – 2 poles – 2850 rpm</div>
  <svg class="charts" width="396" height="553" viewBox="0 0 396 553">
    <defs>
      <pattern id="g1" x="98" y="147" width="10.35" height="6.57" patternUnits="userSpaceOnUse"><path d="M10.35 0V6.57H0" fill="none" stroke="var(--grid)" stroke-width=".35"/></pattern>
      <pattern id="g1e" x="98" y="393" width="10.35" height="5.33" patternUnits="userSpaceOnUse"><path d="M10.35 0V5.33H0" fill="none" stroke="var(--grid)" stroke-width=".35"/></pattern>
    </defs>
    <rect x="98" y="147" width="207" height="230" fill="url(#g1)"/><rect class="frame" x="98" y="147" width="207" height="230"/>
    <text x="86" y="149">H[m]</text><text x="309" y="150">H[ft]</text>
    <g class="axis-end">
      <text x="95" y="379">0</text><text x="95" y="366">20</text><text x="95" y="353">40</text><text x="95" y="340">60</text><text x="95" y="326">80</text><text x="95" y="313">100</text><text x="95" y="300">120</text><text x="95" y="287">140</text><text x="95" y="274">160</text><text x="95" y="261">180</text><text x="95" y="248">200</text><text x="95" y="234">220</text><text x="95" y="221">240</text><text x="95" y="208">260</text><text x="95" y="195">280</text><text x="95" y="182">300</text><text x="95" y="169">320</text><text x="95" y="156">340</text>
    </g>
    <g>
      <text x="309" y="379">0</text><text x="309" y="359">100</text><text x="309" y="339">200</text><text x="309" y="319">300</text><text x="309" y="299">400</text><text x="309" y="279">500</text><text x="309" y="259">600</text><text x="309" y="239">700</text><text x="309" y="219">800</text><text x="309" y="199">900</text><text x="309" y="179">1000</text><text x="309" y="159">1100</text>
    </g>
    <g class="axis-mid">
      <text x="98" y="143">0</text><text x="118" y="143">U.S.GPM</text><text x="147" y="143">2.5</text><text x="196" y="143">5</text><text x="245" y="143">7.5</text><text x="294" y="143">10</text>
      <text x="98" y="385">0</text><text x="124" y="385">5</text><text x="150" y="385">10</text><text x="176" y="385">15</text><text x="202" y="385">20</text><text x="227" y="385">25</text><text x="253" y="385">30</text><text x="279" y="385">35</text><text x="313" y="385">Q [l/min]</text>
    </g>
    <g transform="translate(98,377) scale(5.175,-0.657)">
      <polyline class="curve" vector-effect="non-scaling-stroke" points="0,322 3,314 7,292 10,272 14,240 18,202 21,172 24,142 28,108"/>
      <polyline class="curve" vector-effect="non-scaling-stroke" points="0,255 3,246 7,230 10,214 14,190 18,162 21,138 24,114 28,86"/>
      <polyline class="curve" vector-effect="non-scaling-stroke" points="0,193 3,188 7,177 10,165 14,148 18,126 21,108 24,90 28,68"/>
      <polyline class="curve" vector-effect="non-scaling-stroke" points="0,145 3,140 7,130 10,122 14,110 18,94 21,82 24,68 28,50"/>
      <polyline class="curve" vector-effect="non-scaling-stroke" points="0,115 3,111 7,105 10,98 14,88 18,75 21,65 24,54 28,40"/>
      <polyline class="curve" vector-effect="non-scaling-stroke" points="0,87 3,85 7,80 10,75 14,68 18,58 21,50 24,40 28,28"/>
    </g>
    <g class="pill"><rect x="122" y="183.5" width="24" height="6" rx="3"/><text x="134" y="188.2">33-2HP</text></g>
    <g class="pill"><rect x="122" y="223" width="24" height="6" rx="3"/><text x="134" y="227.7">26-1.5HP</text></g>
    <g class="pill"><rect x="122" y="257.7" width="24" height="6" rx="3"/><text x="134" y="262.4">20-1HP</text></g>
    <g class="pill"><rect x="122" y="288.6" width="24" height="6" rx="3"/><text x="134" y="293.3">15-0.75HP</text></g>
    <g class="pill"><rect x="122" y="305" width="24" height="6" rx="3"/><text x="134" y="309.7">12-0.5HP</text></g>
    <g class="pill"><rect x="122" y="321.4" width="24" height="6" rx="3"/><text x="134" y="326.1">09-0.5HP</text></g>

    <rect x="98" y="393" width="207" height="48" fill="url(#g1e)"/><rect class="frame" x="98" y="393" width="207" height="48"/>
    <text x="70" y="402">η (%)</text>
    <g class="axis-end"><text x="95" y="443">0</text><text x="95" y="427">15</text><text x="95" y="411">30</text><text x="95" y="395">45</text></g>
    <g><text x="309" y="443">0</text><text x="309" y="427">15</text><text x="309" y="411">30</text><text x="309" y="395">45</text></g>
    <g transform="translate(98,441) scale(5.175,-1.067)"><polyline class="curve" vector-effect="non-scaling-stroke" points="0,0 3,11 6,20 9,26 12,31 15,34 18,35 21,34 24,31 28,24"/></g>
    <text x="189" y="405" class="axis-mid">η (%)</text>
    <g class="axis-mid">
      <text x="98" y="449">0</text><text x="124" y="449">5</text><text x="150" y="449">10</text><text x="176" y="449">15</text><text x="202" y="449">20</text><text x="227" y="449">25</text><text x="253" y="449">30</text><text x="279" y="449">35</text><text x="313" y="449">Q [l/min]</text>
    </g>
    <line x1="98" y1="458" x2="305" y2="458" stroke="#666" stroke-width=".5"/>
    <g class="axis-mid">
      <text x="98" y="467">0</text><text x="124" y="467">0.3</text><text x="150" y="467">0.6</text><text x="176" y="467">0.9</text><text x="202" y="467">1.2</text><text x="227" y="467">1.5</text><text x="253" y="467">1.8</text><text x="279" y="467">2.1</text><text x="313" y="467">Q [m³/h]</text>
    </g>
  </svg>
  <table class="spec">
    <thead>
      <tr><th rowspan="3">Type</th><th rowspan="3">N. of<br>Stages</th><th colspan="2">Motor</th><th colspan="3">Pump</th><th>Q</th><th colspan="5">Delivery</th></tr>
      <tr><th rowspan="2">KW</th><th rowspan="2">HP</th><th rowspan="2">Length<br>(mm)</th><th rowspan="2">Outlet<br>(inch)</th><th rowspan="2">Weight<br>(Kg)</th><th>m3/h</th><th>0</th><th>0,3</th><th>0,6</th><th>0,9</th><th>1,2</th></tr>
      <tr><th>l/min</th><th>0</th><th>5</th><th>10</th><th>15</th><th>20</th></tr>
    </thead>
    <tbody>
      <tr><td class="type">KV 1-10</td><td>10</td><td>0,37</td><td>0,50</td><td>348</td><td>1.25"</td><td>3,5</td><td class="head-cell" rowspan="5">Head&nbsp;&nbsp;H m</td><td>67</td><td>63</td><td>55</td><td>46</td><td>33</td></tr>
      <tr><td class="type">KV 1-13</td><td>13</td><td>0,37</td><td>0,50</td><td>402</td><td>1.25"</td><td>4,0</td><td>86</td><td>78</td><td>70</td><td>56</td><td>42</td></tr>
      <tr><td class="type">KV 1-19</td><td>19</td><td>0,55</td><td>0,75</td><td>507</td><td>1.25"</td><td>5,2</td><td>126</td><td>118</td><td>105</td><td>86</td><td>60</td></tr>
      <tr><td class="type">KV 1-26</td><td>26</td><td>0,75</td><td>1,00</td><td>659</td><td>1.25"</td><td>6,8</td><td>173</td><td>160</td><td>141</td><td>117</td><td>81</td></tr>
      <tr><td class="type">KV 1-38</td><td>38</td><td>1,10</td><td>1,50</td><td>868</td><td>1.25"</td><td>8,8</td><td>253</td><td>234</td><td>208</td><td>169</td><td>117</td></tr>
    </tbody>
  </table>
  <div class="folio">10</div>
</section>

<section class="page p11">
  <div class="brand">ORLENTIS</div>
  <div class="band">4” KV 2 | 4” Submersible Pumps | 60 Hz – 2 poles – 3450 rpm</div>
  <svg class="charts" width="396" height="553" viewBox="0 0 396 553">
    <defs>
      <pattern id="g2" x="104" y="121" width="6.19" height="8.72" patternUnits="userSpaceOnUse"><path d="M6.19 0V8.72H0" fill="none" stroke="var(--grid)" stroke-width=".35"/></pattern>
      <pattern id="g2e" x="104" y="353" width="6.19" height="7.67" patternUnits="userSpaceOnUse"><path d="M6.19 0V7.67H0" fill="none" stroke="var(--grid)" stroke-width=".35"/></pattern>
    </defs>
    <rect x="104" y="121" width="198" height="218" fill="url(#g2)"/><rect class="frame" x="104" y="121" width="198" height="218"/>
    <text x="88" y="124">H[m]</text><text x="306" y="124">H[ft]</text>
    <g class="axis-end">
      <text x="101" y="341">0</text><text x="101" y="319">50</text><text x="101" y="297">100</text><text x="101" y="276">150</text><text x="101" y="254">200</text><text x="101" y="232">250</text><text x="101" y="210">300</text><text x="101" y="188">350</text><text x="101" y="167">400</text><text x="101" y="145">450</text>
    </g>
    <g>
      <text x="306" y="341">0</text><text x="306" y="328">100</text><text x="306" y="314">200</text><text x="306" y="301">300</text><text x="306" y="288">400</text><text x="306" y="275">500</text><text x="306" y="261">600</text><text x="306" y="248">700</text><text x="306" y="235">800</text><text x="306" y="221">900</text><text x="306" y="208">1000</text><text x="306" y="195">1100</text><text x="306" y="182">1200</text><text x="306" y="168">1300</text><text x="306" y="155">1400</text><text x="306" y="142">1500</text><text x="306" y="131">1600</text>
    </g>
    <g class="axis-mid">
      <text x="104" y="118">0</text><text x="128" y="118">U.S.GPM</text><text x="151" y="118">5</text><text x="198" y="118">10</text><text x="245" y="118">15</text><text x="291" y="118">20</text>
      <text x="104" y="347">0</text><text x="129" y="347">10</text><text x="154" y="347">20</text><text x="178" y="347">30</text><text x="203" y="347">40</text><text x="228" y="347">50</text><text x="253" y="347">60</text><text x="277" y="347">70</text><text x="311" y="347">Q [l/min]</text>
    </g>
    <g transform="translate(104,339) scale(2.475,-0.436)">
      <polyline class="curve" vector-effect="non-scaling-stroke" points="0,415 10,412 20,400 30,375 40,332 50,268 60,188 70,100"/>
      <polyline class="curve" vector-effect="non-scaling-stroke" points="0,340 10,335 20,322 30,297 40,258 50,205 60,142 70,72"/>
      <polyline class="curve" vector-effect="non-scaling-stroke" points="0,270 10,265 20,255 30,236 40,204 50,162 60,112 70,56"/>
      <polyline class="curve" vector-effect="non-scaling-stroke" points="0,198 10,193 20,185 30,171 40,149 50,119 60,82 70,43"/>
      <polyline class="curve" vector-effect="non-scaling-stroke" points="0,170 10,166 20,158 30,146 40,126 50,101 60,70 70,35"/>
      <polyline class="curve" vector-effect="non-scaling-stroke" points="0,117 10,115 20,110 30,101 40,88 50,71 60,49 70,26"/>
      <polyline class="curve" vector-effect="non-scaling-stroke" points="0,97 10,95 20,90 30,83 40,72 50,58 60,40 70,20"/>
      <polyline class="curve" vector-effect="non-scaling-stroke" points="0,67 10,66 20,63 30,58 40,50 50,40 60,28 70,14"/>
      <polyline class="curve" vector-effect="non-scaling-stroke" points="0,47 10,46 20,44 30,40 40,35 50,28 60,19 70,10"/>
    </g>
    <g class="pill"><rect x="117" y="156.4" width="24" height="6" rx="3"/><text x="129" y="161.1">42-5HP</text></g>
    <g class="pill"><rect x="117" y="190" width="24" height="6" rx="3"/><text x="129" y="194.7">34-4HP</text></g>
    <g class="pill"><rect x="117" y="220.5" width="24" height="6" rx="3"/><text x="129" y="225.2">27-3HP</text></g>
    <g class="pill"><rect x="117" y="251.9" width="24" height="6" rx="3"/><text x="129" y="256.6">20-2HP</text></g>
    <g class="pill"><rect x="117" y="263.6" width="24" height="6" rx="3"/><text x="129" y="268.3">17-1.5HP</text></g>
    <g class="pill"><rect x="117" y="285.9" width="24" height="6" rx="3"/><text x="129" y="290.6">12-1HP</text></g>
    <g class="pill"><rect x="117" y="294.6" width="24" height="6" rx="3"/><text x="129" y="299.3">10-0.75HP</text></g>
    <g class="pill"><rect x="117" y="304.2" width="24" height="6" rx="3"/><text x="129" y="308.9">07-0.5HP</text></g>
    <g class="pill"><rect x="117" y="313" width="24" height="6" rx="3"/><text x="129" y="317.7">05-0.5HP</text></g>

    <rect x="104" y="353" width="198" height="46" fill="url(#g2e)"/><rect class="frame" x="104" y="353" width="198" height="46"/>
    <text x="78" y="362">η (%)</text>
    <g class="axis-end"><text x="101" y="401">0</text><text x="101" y="386">20</text><text x="101" y="370">40</text><text x="101" y="355">60</text></g>
    <g><text x="306" y="401">0</text><text x="306" y="386">20</text><text x="306" y="370">40</text><text x="306" y="355">60</text></g>
    <g transform="translate(104,399) scale(2.475,-0.767)"><polyline class="curve" vector-effect="non-scaling-stroke" points="0,0 8,14 16,27 24,38 32,47 40,52 46,53 52,51 58,45 64,37 70,27"/></g>
    <text x="215" y="366" class="axis-mid">η (%)</text>
    <g class="axis-mid">
      <text x="104" y="407">0</text><text x="129" y="407">10</text><text x="154" y="407">20</text><text x="178" y="407">30</text><text x="203" y="407">40</text><text x="228" y="407">50</text><text x="253" y="407">60</text><text x="277" y="407">70</text><text x="311" y="407">Q [l/min]</text>
    </g>
    <line x1="104" y1="414" x2="302" y2="414" stroke="#666" stroke-width=".5"/>
    <g class="axis-mid">
      <text x="104" y="423">0</text><text x="129" y="423">0.6</text><text x="154" y="423">1.2</text><text x="178" y="423">1.8</text><text x="203" y="423">2.4</text><text x="228" y="423">3</text><text x="253" y="423">3.6</text><text x="277" y="423">4.2</text><text x="311" y="423">Q [m³/h]</text>
    </g>
  </svg>
  <table class="spec">
    <thead>
      <tr><th rowspan="3">Type</th><th rowspan="3">N. of<br>Stages</th><th colspan="2">Motor</th><th colspan="3">Pump</th><th>Q</th><th colspan="6">Delivery</th></tr>
      <tr><th rowspan="2">KW</th><th rowspan="2">HP</th><th rowspan="2">Length<br>(mm)</th><th rowspan="2">Outlet<br>(inch)</th><th rowspan="2">Weight<br>(Kg)</th><th>m3/h</th><th>0</th><th>1,5</th><th>1,8</th><th>2,1</th><th>2,4</th><th>2,7</th></tr>
      <tr><th>l/min</th><th>0</th><th>25</th><th>30</th><th>35</th><th>40</th><th>45</th></tr>
    </thead>
    <tbody>
      <tr><td class="type">KV 2-5</td><td>5</td><td>0,37</td><td>0,50</td><td>261</td><td>1.25"</td><td>2,5</td><td class="head-cell" rowspan="7">Head&nbsp;&nbsp;&nbsp;H m</td><td>33</td><td>28</td><td>26</td><td>24</td><td>20</td><td>17</td></tr>
      <tr><td class="type">KV 2-7</td><td>7</td><td>0,37</td><td>0,50</td><td>297</td><td>1.25"</td><td>3,0</td><td>47</td><td>39</td><td>35</td><td>32</td><td>28</td><td>24</td></tr>
      <tr><td class="type">KV 2-10</td><td>10</td><td>0,55</td><td>0,75</td><td>349</td><td>1.25"</td><td>3,5</td><td>67</td><td>56</td><td>52</td><td>47</td><td>41</td><td>35</td></tr>
      <tr><td class="type">KV 2-14</td><td>14</td><td>0,75</td><td>1,00</td><td>418</td><td>1.25"</td><td>4,8</td><td>93</td><td>78</td><td>73</td><td>66</td><td>57</td><td>50</td></tr>
      <tr><td class="type">KV 2-20</td><td>20</td><td>1,10</td><td>1,50</td><td>523</td><td>1.25"</td><td>5,3</td><td>133</td><td>113</td><td>104</td><td>97</td><td>82</td><td>72</td></tr>
      <tr><td class="type">KV 2-28</td><td>28</td><td>1,50</td><td>2,00</td><td>702</td><td>1.25"</td><td>6,9</td><td>187</td><td>158</td><td>146</td><td>130</td><td>115</td><td>97</td></tr>
      <tr><td class="type">KV 2-40</td><td>40</td><td>2,20</td><td>3,00</td><td>901</td><td>1.25"</td><td>9,0</td><td>267</td><td>226</td><td>208</td><td>186</td><td>164</td><td>136</td></tr>
    </tbody>
  </table>
  <div class="folio">11</div>
</section>

<section class="page p12">
  <div class="brand">ORLENTIS</div>
  <div class="band">4” KV 3 | 4” Submersible Pumps | 60 Hz – 2 poles – 3450 rpm</div>
  <svg class="charts" width="396" height="553" viewBox="0 0 396 553">
    <defs>
      <pattern id="g3" x="100" y="122" width="9.9" height="8.68" patternUnits="userSpaceOnUse"><path d="M9.9 0V8.68H0" fill="none" stroke="var(--grid)" stroke-width=".35"/></pattern>
      <pattern id="g3e" x="100" y="355" width="9.9" height="5.875" patternUnits="userSpaceOnUse"><path d="M9.9 0V5.875H0" fill="none" stroke="var(--grid)" stroke-width=".35"/></pattern>
    </defs>
    <rect x="100" y="122" width="198" height="217" fill="url(#g3)"/><rect class="frame" x="100" y="122" width="198" height="217"/>
    <text x="82" y="126" style="font-size:6.5px">H[m]</text><text x="302" y="128" style="font-size:6.5px">H[ft]</text>
    <g class="axis-end">
      <text x="97" y="341">0</text><text x="97" y="324">20</text><text x="97" y="306">40</text><text x="97" y="289">60</text><text x="97" y="272">80</text><text x="97" y="254">100</text><text x="97" y="237">120</text><text x="97" y="219">140</text><text x="97" y="202">160</text><text x="97" y="185">180</text><text x="97" y="167">200</text><text x="97" y="150">220</text><text x="97" y="133">240</text>
    </g>
    <g>
      <text x="303" y="341">0</text><text x="303" y="315">100</text><text x="303" y="288">200</text><text x="303" y="262">300</text><text x="303" y="235">400</text><text x="303" y="209">500</text><text x="303" y="182">600</text><text x="303" y="156">700</text><text x="303" y="134">800</text>
    </g>
    <g class="axis-mid">
      <text x="100" y="119">0</text><text x="120" y="119">U.S.GPM</text><text x="137" y="119">5</text><text x="175" y="119">10</text><text x="250" y="119">20</text><text x="287" y="119">25</text>
      <text x="100" y="347">0</text><text x="120" y="347">10</text><text x="140" y="347">20</text><text x="159" y="347">30</text><text x="179" y="347">40</text><text x="199" y="347">50</text><text x="219" y="347">60</text><text x="239" y="347">70</text><text x="258" y="347">80</text><text x="278" y="347">90</text><text x="308" y="347">Q [l/min]</text>
    </g>
    <g transform="translate(100,339) scale(1.98,-0.868)">
      <polyline class="curve" vector-effect="non-scaling-stroke" points="0,210 10,208 20,201 30,184 40,157 50,127 60,96 70,63"/>
      <polyline class="curve" vector-effect="non-scaling-stroke" points="0,142 10,141 20,135 30,125 40,110 50,91 60,70 70,48"/>
      <polyline class="curve" vector-effect="non-scaling-stroke" points="0,105 10,104 20,100 30,92 40,80 50,66 60,52 70,35"/>
      <polyline class="curve" vector-effect="non-scaling-stroke" points="0,72 10,71 20,68 30,63 40,55 50,46 60,37 70,26"/>
      <polyline class="curve" vector-effect="non-scaling-stroke" points="0,55 10,54 20,52 30,48 40,42 50,35 60,28 70,20"/>
      <polyline class="curve" vector-effect="non-scaling-stroke" points="0,33 10,33 20,32 30,30 40,27 50,23 60,19 70,13"/>
    </g>
    <g class="pill"><rect x="113" y="157.5" width="30" height="7" rx="3.5"/><text x="128" y="162.6" style="font-size:5px">32-3HP</text></g>
    <g class="pill"><rect x="113" y="213.1" width="30" height="7" rx="3.5"/><text x="128" y="218.2" style="font-size:5px">21-2HP</text></g>
    <g class="pill"><rect x="113" y="245.2" width="30" height="7" rx="3.5"/><text x="128" y="250.3" style="font-size:5px">16-1.5HP</text></g>
    <g class="pill"><rect x="113" y="273.9" width="30" height="7" rx="3.5"/><text x="128" y="279" style="font-size:5px">11-1HP</text></g>
    <g class="pill"><rect x="113" y="288.6" width="30" height="7" rx="3.5"/><text x="128" y="293.7" style="font-size:5px">08-0.75HP</text></g>
    <g class="pill"><rect x="113" y="306.9" width="30" height="7" rx="3.5"/><text x="128" y="312" style="font-size:5px">05-0.5HP</text></g>

    <rect x="100" y="355" width="198" height="47" fill="url(#g3e)"/><rect class="frame" x="100" y="355" width="198" height="47"/>
    <text x="80" y="360">%)</text>
    <g class="axis-end"><text x="97" y="404">0</text><text x="97" y="392">20</text><text x="97" y="380">40</text><text x="97" y="369">60</text><text x="97" y="357">80</text></g>
    <g><text x="303" y="404">0</text><text x="303" y="392">20</text><text x="303" y="380">40</text><text x="303" y="369">60</text><text x="303" y="357">80</text></g>
    <g transform="translate(100,402) scale(1.98,-0.5875)"><polyline class="curve" vector-effect="non-scaling-stroke" points="0,0 8,14 16,27 24,38 32,47 40,53 46,55 52,55 58,53 64,48 70,40"/></g>
    <text x="191" y="370" class="axis-mid">η (%)</text>
    <g class="axis-mid">
      <text x="100" y="410">0</text><text x="120" y="410">10</text><text x="140" y="410">20</text><text x="159" y="410">30</text><text x="179" y="410">40</text><text x="199" y="410">50</text><text x="219" y="410">60</text><text x="239" y="410">70</text><text x="258" y="410">80</text><text x="278" y="410">90</text><text x="308" y="410">Q [l/min]</text>
    </g>
    <line x1="100" y1="416" x2="298" y2="416" stroke="#666" stroke-width=".5"/>
    <g class="axis-mid">
      <text x="100" y="425">0</text><text x="120" y="425">0.6</text><text x="140" y="425">1.2</text><text x="159" y="425">1.8</text><text x="179" y="425">2.4</text><text x="199" y="425">3</text><text x="219" y="425">3.6</text><text x="239" y="425">4.2</text><text x="258" y="425">4.8</text><text x="278" y="425">5.4</text><text x="308" y="425">Q [m³/h]</text>
    </g>
  </svg>
  <table class="spec">
    <thead>
      <tr><th rowspan="3">Type</th><th rowspan="3">N. of<br>Stages</th><th colspan="2">Motor</th><th colspan="3">Pump</th><th>Q</th><th colspan="6">Delivery</th></tr>
      <tr><th rowspan="2">KW</th><th rowspan="2">HP</th><th rowspan="2">Length<br>(mm)</th><th rowspan="2">Outlet<br>(inch)</th><th rowspan="2">Weight<br>(Kg)</th><th>m3/h</th><th>0</th><th>2,1</th><th>2,4</th><th>2,7</th><th>3,0</th><th>3,6</th></tr>
      <tr><th>l/min</th><th>0</th><th>35</th><th>40</th><th>45</th><th>50</th><th>60</th></tr>
    </thead>
    <tbody>
      <tr><td class="type">KV 3-5</td><td>5</td><td>0,37</td><td>0,50</td><td>261</td><td>1.25"</td><td>2,6</td><td class="head-cell" rowspan="6">Head&nbsp;&nbsp;&nbsp;H m</td><td>34</td><td>29</td><td>27</td><td>25</td><td>23</td><td>18</td></tr>
      <tr><td class="type">KV 3-8</td><td>8</td><td>0,55</td><td>0,75</td><td>314</td><td>1.25"</td><td>3,1</td><td>54</td><td>46</td><td>43</td><td>41</td><td>38</td><td>30</td></tr>
      <tr><td class="type">KV 3-11</td><td>11</td><td>0,75</td><td>1,00</td><td>366</td><td>1.25"</td><td>3,7</td><td>72</td><td>61</td><td>58</td><td>54</td><td>49</td><td>38</td></tr>
      <tr><td class="type">KV 3-16</td><td>16</td><td>1,10</td><td>1,50</td><td>453</td><td>1.25"</td><td>4,6</td><td>106</td><td>89</td><td>83</td><td>77</td><td>70</td><td>54</td></tr>
      <tr><td class="type">KV 3-21</td><td>21</td><td>1,50</td><td>2,00</td><td>540</td><td>1.25"</td><td>5,5</td><td>142</td><td>122</td><td>115</td><td>108</td><td>100</td><td>79</td></tr>
      <tr><td class="type">KV 3-32</td><td>32</td><td>2,20</td><td>3,00</td><td>761</td><td>1.25"</td><td>7,6</td><td>208</td><td>177</td><td>165</td><td>152</td><td>138</td><td>104</td></tr>
    </tbody>
  </table>
  <div class="folio">12</div>
</section>

</body>
</html>
```